Business Brochure for Mobile Fleet Mechanic Company

Make a brochure for an mobile mechanic company that is a Bi-fold 8.5"Wx11"H. A Bi-fold would have the outside and inside design so it is a total of 4 pages at 8.5"x11". The print is 2-sides 17"Wx11"H that folds down to 8.5"Wx11"H.
Should have photo of mechanic working. Blue in logo is Pantone 284C. Will provide text to be added to approved design.

Contact Information for Business Card

2-sided card using the same design elements and colors as the brochure.

```html
<!DOCTYPE html>
<html lang="en">
<head>
<meta charset="utf-8">
<title>HaulWell Fleet Maintenance Brochure</title>
<link href="https://fonts.googleapis.com/css2?family=Oswald:wght@400;500;600&family=Open+Sans:wght@400;600&display=swap" rel="stylesheet">
<style>
:root{
  --stage:#a7a9ad;
  --ink:#1b1b1d;
  --dark:#1c1d20;
  --paper:#f2f3f5;
  --paper-2:#e4e7eb;
  --blue:#1d5ea8;
  --blue-deep:#0f4a8c;
  --sky:#5d9ad8;
  --cyan:#1b9be2;
  --grey-text:#3d4045;
  --white:#ffffff;
}
*{margin:0;padding:0;box-sizing:border-box}
html,body{width:916px;height:1200px;overflow:hidden}
body{background:var(--stage);font-family:"Open Sans",Arial,sans-serif;position:relative}
.spread{position:absolute;left:58px;width:805px;height:520px;background:var(--paper);overflow:hidden}
.spread--outside{top:63px}
.spread--inside{top:626px}
.abs{position:absolute}
.head{font-family:"Oswald",Arial,sans-serif;text-transform:uppercase;white-space:nowrap}
.photo{position:absolute}

/* outside spread */
.top-band{left:0;top:0;width:402px;height:98px;background:var(--white)}
.cover-title{left:0;top:22px;width:402px;text-align:center;color:var(--sky);font-size:20px;font-weight:500;letter-spacing:.2px}
.cover-sub{left:0;top:53px;width:402px;text-align:center;color:var(--ink);font-size:10px;font-weight:500}
.dark-band{left:0;top:98px;width:402px;height:251px;background:var(--dark)}
.section-title{color:var(--sky);font-size:14px;font-weight:500}
.mobile-title{left:22px;top:114px}
.body-copy{color:#e8e8e8;font-size:8.4px;line-height:11.8px;text-align:justify}
.mobile-copy{left:22px;top:140px;width:218px}
.mechanic-photo{left:10px;top:208px;width:220px;height:226px;background:linear-gradient(180deg,#3c4a6a,#283552)}
.sedan-photo{left:222px;top:288px;width:176px;height:110px;background:radial-gradient(ellipse at 50% 55%,#e6e8ec,#a9adb4 70%,transparent 72%)}
.contact-list{left:22px;top:452px;color:var(--white);font-size:13px;font-weight:600;list-style:none;white-space:nowrap}
.contact-list li{display:flex;align-items:center;gap:8px;height:21px}
.icon-box{width:14px;height:14px;border-radius:2px;background:var(--sky);display:inline-flex;align-items:center;justify-content:center}
.brand{display:flex;align-items:center;gap:7px;font-family:"Oswald",Arial,sans-serif;font-weight:600;color:var(--sky);white-space:nowrap}
.brand-dot{border-radius:50%;background:var(--sky)}
.brand--back{left:262px;top:480px;font-size:28px}
.brand--back .brand-dot{width:14px;height:14px}
.brand--front{left:420px;top:32px;font-size:32px}
.brand--front .brand-dot{width:16px;height:16px}
.front-top{left:402px;top:0;width:403px;height:98px;background:var(--white)}
.front-tag{left:612px;top:40px;color:var(--sky);font-size:17px;font-style:italic;line-height:24px}
.trucks-photo{left:402px;top:98px;width:403px;height:252px;background:linear-gradient(160deg,#2f4f7c 0%,#1a2c46 55%,#0c1422 100%)}
.front-lower{left:402px;top:350px;width:403px;height:170px;background:linear-gradient(180deg,#f4f5f7,#dfe3e8)}
.front-title{left:402px;top:372px;width:403px;text-align:center;color:#2a2b2f;font-size:34px;font-weight:500}
.front-sub{left:402px;top:427px;width:403px;text-align:center;color:var(--sky);font-size:9px;font-weight:500}
.web-small{left:436px;top:487px;color:var(--grey-text);font-size:8px;letter-spacing:2px;white-space:nowrap}
.phone-big{color:var(--white);font-family:"Oswald",Arial,sans-serif;font-size:22px;font-weight:500;display:flex;align-items:center;gap:10px;white-space:nowrap;left:646px;top:481px}

/* inside spread */
.inside-photo{left:380px;top:0;width:425px;height:250px;background:linear-gradient(120deg,#cfd6df 0%,#8fa0b6 45%,#1f3f7a 75%,#1b3566 100%)}
.bubble{width:112px;height:112px;border-radius:50%;border:4px solid var(--white);box-shadow:0 0 0 2px var(--sky);background:radial-gradient(circle,#6c7786,#2d3440)}
.inside-lower{left:0;top:250px;width:805px;height:270px;background:linear-gradient(180deg,#f5f6f8,#e3e6ea)}
.repair-title{left:22px;top:30px;font-size:18px}
.repair-copy{left:22px;top:60px;width:352px}
.checks{list-style:none}
.checks li{display:flex;align-items:center;gap:8px;font-family:"Oswald",Arial,sans-serif;text-transform:uppercase;font-size:9px;height:18.4px;white-space:nowrap}
.checks--dark{left:22px;top:136px;color:var(--white)}
.checks--light{color:#4a4d52}
.list-title{left:22px;top:274px;color:#26272b;font-size:12px;font-weight:500;display:flex;align-items:center;gap:6px}
.list-title span.arrow{color:var(--sky);font-size:14px}
.service-list{left:37px;top:300px;list-style:none;color:var(--grey-text);font-size:9px;line-height:13.1px;white-space:nowrap}
.suv-photo{left:214px;top:354px;width:180px;height:130px;background:radial-gradient(ellipse at 50% 50%,#5a5d63,#2c2e33 65%,transparent 68%)}
.pro-title{left:418px;top:274px;color:var(--sky);font-size:11.5px;font-weight:500;line-height:16px}
.pro-copy{left:418px;top:316px;width:370px;color:var(--grey-text);font-size:8.3px;line-height:12.6px;text-align:justify}
.strip{top:503px;height:17px;background:var(--cyan)}
</style>
</head>
<body>

<section class="spread spread--outside">
  <div class="abs top-band"></div>
  <h2 class="abs head cover-title">Full-Service Fleet Maintenance</h2>
  <p class="abs head cover-sub">Keep your vehicles running</p>

  <div class="abs dark-band"></div>
  <svg class="abs" style="left:0;top:98px" width="402" height="251" aria-hidden="true">
    <polygon points="290,0 330,0 130,251 90,251" fill="#1f4f8f" opacity=".55"/>
    <polygon points="340,0 352,0 152,251 140,251" fill="#2a6ab8" opacity=".7"/>
    <polygon points="360,0 402,0 402,40 222,251 180,251" fill="#173f73" opacity=".6"/>
  </svg>
  <h3 class="abs head section-title mobile-title">Mobile Fleet Mechanic</h3>
  <p class="abs body-copy mobile-copy">HaulWell offers full repairs for trucks and other fleet vehicles so that you stay safe on the road. Our factory-certified team will make sure you get the attention you need for your fleet vehicles<br>CONTACT US TODAY FOR AN APPOINTMENT.</p>

  <div class="photo mechanic-photo" role="img" aria-label="Smiling mechanic in navy overalls holding a wrench, arms crossed"></div>
  <div class="photo sedan-photo" role="img" aria-label="Silver sedan, front three-quarter view"></div>

  <svg class="abs" style="left:0;top:434px" width="282" height="86" aria-hidden="true">
    <polygon points="0,0 282,0 222,86 0,86" fill="#2b2c30"/>
  </svg>
  <ul class="abs contact-list">
    <li><span class="icon-box"><svg width="9" height="9" viewBox="0 0 24 24"><path d="M6.6 10.8a15 15 0 006.6 6.6l2.2-2.2c.3-.3.7-.4 1-.2 1.1.4 2.3.6 3.6.6.6 0 1 .4 1 1V20c0 .6-.4 1-1 1A17 17 0 013 4c0-.6.4-1 1-1h3.5c.6 0 1 .4 1 1 0 1.3.2 2.5.6 3.6.1.3 0 .7-.2 1z" fill="#fff"/></svg></span>555 014 2207</li>
    <li><span class="icon-box"><svg width="9" height="9" viewBox="0 0 24 24"><rect x="2" y="5" width="20" height="14" fill="none" stroke="#fff" stroke-width="2.5"/><path d="M2 5l10 8 10-8" fill="none" stroke="#fff" stroke-width="2.5"/></svg></span>service@haulwellfleet.com</li>
    <li><span class="icon-box"><svg width="9" height="9" viewBox="0 0 24 24"><circle cx="12" cy="12" r="9" fill="none" stroke="#fff" stroke-width="2.5"/></svg></span>www.haulwellfleet.com</li>
  </ul>
  <div class="abs brand brand--back"><span class="brand-dot"></span>HaulWell</div>

  <div class="abs front-top"></div>
  <svg class="abs" style="left:402px;top:0" width="403" height="98" aria-hidden="true">
    <polygon points="200,0 403,0 403,98 170,98" fill="#2d2f33"/>
  </svg>
  <div class="abs brand brand--front"><span class="brand-dot"></span>HaulWell</div>
  <p class="abs head front-tag">Full-Service<br>Fleet Maintenance</p>

  <div class="photo trucks-photo" role="img" aria-label="Row of blue fleet trucks lined up at dusk"></div>
  <div class="abs front-lower"></div>
  <h1 class="abs head front-title">Truck and Auto Repairs</h1>
  <p class="abs head front-sub">For complete fleet repairs, call us today!</p>
  <p class="abs web-small">www.haulwellfleet.com</p>

  <div class="abs strip" style="left:402px;width:403px"></div>
  <svg class="abs" style="left:402px;top:470px" width="403" height="50" aria-hidden="true">
    <polygon points="190,0 403,0 403,50 150,50" fill="var(--blue-deep)"/>
  </svg>
  <div class="abs phone-big">
    <svg width="22" height="22" viewBox="0 0 24 24"><circle cx="12" cy="12" r="10.5" fill="none" stroke="#fff" stroke-width="1.8"/><path d="M8.5 7l1.6 2.4-1 1a7 7 0 003.5 3.5l1-1 2.4 1.6-.9 1.8c-3.4-.4-7.3-4.3-7.7-7.7z" fill="#fff"/></svg>
    <span>555 014 2207</span>
  </div>
</section>

<section class="spread spread--inside">
  <div class="photo inside-photo" role="img" aria-label="Mechanic in blue uniform holding a large wrench in a busy workshop"></div>
  <svg class="abs" style="left:0;top:0" width="480" height="250" aria-hidden="true">
    <polygon points="0,0 422,0 302,250 0,250" fill="var(--dark)"/>
    <polygon points="430,0 446,0 326,250 310,250" fill="#6b6e73"/>
    <polygon points="452,0 462,0 342,250 332,250" fill="#ffffff"/>
    <polygon points="468,0 480,0 360,250 348,250" fill="#8a8d92"/>
  </svg>
  <h2 class="abs head section-title repair-title">Efficient Fleet Repair</h2>
  <p class="abs body-copy repair-copy">Getting repairs done on time for your fleet is a smart investment in your business. Regular maintenance can help prevent downtime, as the team at HaulWell Service Co will be able to identify problems before they impact your business. We have a variety of fleet repair options available to handle fleets of any size. Getting the small things taken care of can prevent more expensive repairs down the road.</p>
  <ul class="abs checks checks--dark">
    <li><svg width="10" height="10" viewBox="0 0 10 10"><rect x=".5" y=".5" width="9" height="9" fill="none" stroke="#5d9ad8"/><path d="M2 5l2 2 5-5" fill="none" stroke="#5d9ad8" stroke-width="1.3"/></svg>Preventative maintenance</li>
    <li><svg width="10" height="10" viewBox="0 0 10 10"><rect x=".5" y=".5" width="9" height="9" fill="none" stroke="#5d9ad8"/><path d="M2 5l2 2 5-5" fill="none" stroke="#5d9ad8" stroke-width="1.3"/></svg>D.O.T. inspections</li>
    <li><svg width="10" height="10" viewBox="0 0 10 10"><rect x=".5" y=".5" width="9" height="9" fill="none" stroke="#5d9ad8"/><path d="M2 5l2 2 5-5" fill="none" stroke="#5d9ad8" stroke-width="1.3"/></svg>MD PM inspections</li>
    <li><svg width="10" height="10" viewBox="0 0 10 10"><rect x=".5" y=".5" width="9" height="9" fill="none" stroke="#5d9ad8"/><path d="M2 5l2 2 5-5" fill="none" stroke="#5d9ad8" stroke-width="1.3"/></svg>All types of mechanical repairs</li>
    <li><svg width="10" height="10" viewBox="0 0 10 10"><rect x=".5" y=".5" width="9" height="9" fill="none" stroke="#5d9ad8"/><path d="M2 5l2 2 5-5" fill="none" stroke="#5d9ad8" stroke-width="1.3"/></svg>Trailer repairs</li>
  </ul>

  <div class="abs inside-lower"></div>
  <div class="abs bubble" role="img" aria-label="Vehicle raised on a lift with brake assembly exposed" style="left:542px;top:162px"></div>
  <div class="abs bubble" role="img" aria-label="Hand using a ratchet on an engine" style="left:674px;top:162px"></div>

  <h3 class="abs head list-title"><span class="arrow">»</span>Full list of auto and truck repair services</h3>
  <ul class="abs service-list">
    <li>Brakes, alignment, shocks, and struts</li>
    <li>Alternators and batteries</li>
    <li>Starters and water pumps</li>
    <li>Thermostats and radiators</li>
    <li>Hoses, belts, and fuel pumps</li>
    <li>Electrical problems</li>
    <li>CJ joints, engines, and transmissions</li>
    <li>Diagnostics</li>
    <li>D.O.T. inspections</li>
    <li>Liftgate repairs</li>
    <li>Minor body repairs</li>
    <li>Major engine repairs</li>
    <li>Transmission and differentials</li>
    <li>Trailer repairs</li>
    <li>Exhaust repairs</li>
  </ul>
  <div class="photo suv-photo" role="img" aria-label="Dark grey SUV, front three-quarter view"></div>

  <h3 class="abs head pro-title">Professional,<br>High-quality fleet work</h3>
  <p class="abs pro-copy">Make sure your company's fleet of vehicles is something you can be proud of. HaulWell Service Co offers diagnostics and repairs from factory-certified technicians that are trained in the latest software and diagnostic tools. We specialize in maintaining corporate accounts and working with national leasing companies, which is a testament to the high-quality work and attention to detail we offer.</p>
  <ul class="abs checks checks--light" style="left:418px;top:384px">
    <li><svg width="10" height="10" viewBox="0 0 10 10"><rect x=".5" y=".5" width="9" height="9" fill="none" stroke="#5d9ad8"/><path d="M2 5l2 2 5-5" fill="none" stroke="#5d9ad8" stroke-width="1.3"/></svg>Scheduled maintenance</li>
    <li><svg width="10" height="10" viewBox="0 0 10 10"><rect x=".5" y=".5" width="9" height="9" fill="none" stroke="#5d9ad8"/><path d="M2 5l2 2 5-5" fill="none" stroke="#5d9ad8" stroke-width="1.3"/></svg>Brake system inspections &amp; repairs</li>
    <li><svg width="10" height="10" viewBox="0 0 10 10"><rect x=".5" y=".5" width="9" height="9" fill="none" stroke="#5d9ad8"/><path d="M2 5l2 2 5-5" fill="none" stroke="#5d9ad8" stroke-width="1.3"/></svg>Transmission</li>
    <li><svg width="10" height="10" viewBox="0 0 10 10"><rect x=".5" y=".5" width="9" height="9" fill="none" stroke="#5d9ad8"/><path d="M2 5l2 2 5-5" fill="none" stroke="#5d9ad8" stroke-width="1.3"/></svg>Air conditioning and heating</li>
  </ul>
  <ul class="abs checks checks--light" style="left:600px;top:384px">
    <li><svg width="10" height="10" viewBox="0 0 10 10"><rect x=".5" y=".5" width="9" height="9" fill="none" stroke="#5d9ad8"/><path d="M2 5l2 2 5-5" fill="none" stroke="#5d9ad8" stroke-width="1.3"/></svg>Engine repair</li>
    <li><svg width="10" height="10" viewBox="0 0 10 10"><rect x=".5" y=".5" width="9" height="9" fill="none" stroke="#5d9ad8"/><path d="M2 5l2 2 5-5" fill="none" stroke="#5d9ad8" stroke-width="1.3"/></svg>Electrical and computer diagnostics</li>
    <li><svg width="10" height="10" viewBox="0 0 10 10"><rect x=".5" y=".5" width="9" height="9" fill="none" stroke="#5d9ad8"/><path d="M2 5l2 2 5-5" fill="none" stroke="#5d9ad8" stroke-width="1.3"/></svg>Fuel systems (gas and diesel)</li>
  </ul>

  <div class="abs strip" style="left:0;width:805px"></div>
  <svg class="abs" style="left:402px;top:470px" width="403" height="50" aria-hidden="true">
    <polygon points="190,0 403,0 403,50 150,50" fill="var(--blue-deep)"/>
  </svg>
  <div class="abs phone-big">
    <svg width="22" height="22" viewBox="0 0 24 24"><circle cx="12" cy="12" r="10.5" fill="none" stroke="#fff" stroke-width="1.8"/><path d="M8.5 7l1.6 2.4-1 1a7 7 0 003.5 3.5l1-1 2.4 1.6-.9 1.8c-3.4-.4-7.3-4.3-7.7-7.7z" fill="#fff"/></svg>
    <span>555 014 2207</span>
  </div>
</section>

</body>
</html>
```